7 variations of an already existing packet design needed

i need 8 colour and flavour variations of a design that i have already in AI/PDF/PSD format

i need 7 colour variations of the packet with the names of the flavours incorporated onto the packaging itself.

the 7 colour/flavour variations i want are

pineapple
cherry
blueberry
bubblegum
strawberry
menthol
mango
Apple & Blackcurrant

Requirements
Must have
• Must use the original design and have different colour anf flavour variations as described in the brief.
Should not have
• Not be an original design

```html
<!DOCTYPE html>
<html lang="en">
<head>
<meta charset="utf-8">
<title>Velvet Haze – Flavour Range</title>
<link href="https://fonts.googleapis.com/css2?family=Roboto+Condensed:wght@700&family=Arimo:wght@400&display=swap" rel="stylesheet">
<style>
  :root {
    --paper: #ffffff;
    --rule: #3a3a3a;
    --ink-dim: #111111;
    --blackcurrant: #111111;
    --blueberry: #0b4a8c;
    --bubblegum: #d4145a;
    --cherry: #5a2539;
    --mango: #e8663a;
    --menthol: #1f5c2b;
    --pineapple: #fbb040;
    --strawberry: #b02a32;
  }
  html, body {
    margin: 0;
    padding: 0;
    width: 1200px;
    height: 2268px;
    overflow: hidden;
    background: var(--paper);
  }
  .sheet {
    position: relative;
    width: 1200px;
    height: 2268px;
    display: grid;
    grid-template-columns: 600px 600px;
    grid-template-rows: repeat(4, 567px);
    box-sizing: border-box;
  }
  .pack {
    position: relative;
    box-sizing: border-box;
    border-right: 2px solid var(--rule);
    border-bottom: 2px solid var(--rule);
    overflow: hidden;
  }
  .pack:nth-child(2n) { border-right: none; }
  .pack:nth-last-child(-n+2) { border-bottom: none; }

  .smoke {
    position: absolute;
    left: 120px;
    top: 20px;
    width: 400px;
    height: 520px;
    border-radius: 48% 52% 40% 60% / 55% 45% 55% 45%;
    background: radial-gradient(ellipse at 45% 50%, var(--tint) 0%, transparent 70%);
    opacity: 0.22;
  }
  .badge {
    position: absolute;
    left: 190px;
    top: 110px;
    width: 220px;
    display: flex;
    flex-direction: column;
    align-items: center;
    color: var(--tint);
    font-family: "Roboto Condensed", "Arial Narrow", sans-serif;
    font-weight: 700;
    text-transform: uppercase;
    text-align: center;
  }
  .badge__dot {
    width: 46px;
    height: 46px;
    border-radius: 50%;
    background: var(--tint);
    margin-bottom: 40px;
  }
  .badge__name {
    font-size: 54px;
    line-height: 1;
    letter-spacing: 1px;
  }
  .badge__flavour {
    margin-top: 26px;
    font-size: 22px;
    line-height: 1.15;
    letter-spacing: 1px;
  }

  .pack--blackcurrant { --tint: var(--blackcurrant); }
  .pack--blueberry { --tint: var(--blueberry); }
  .pack--bubblegum { --tint: var(--bubblegum); }
  .pack--cherry { --tint: var(--cherry); }
  .pack--mango { --tint: var(--mango); }
  .pack--menthol { --tint: var(--menthol); }
  .pack--pineapple { --tint: var(--pineapple); }
  .pack--strawberry { --tint: var(--strawberry); }

  .dimension {
    position: absolute;
    font-family: "Arimo", Arial, sans-serif;
    font-size: 22px;
    color: var(--ink-dim);
  }
  .dimension--width { left: 1012px; top: 570px; }
  .dimension--height {
    left: 586px;
    top: 820px;
    transform: rotate(-90deg);
    transform-origin: center;
  }
</style>
</head>
<body>
<main class="sheet">
  <section class="pack pack--blackcurrant">
    <div class="smoke" role="img" aria-label="Soft smoke swirl decoration in grey"></div>
    <div class="badge"><span class="badge__dot"></span><span class="badge__name">Velvet Haze</span><span class="badge__flavour">Blackcurrant<br>&amp; Apple</span></div>
  </section>
  <section class="pack pack--blueberry">
    <div class="smoke" role="img" aria-label="Soft smoke swirl decoration in blue"></div>
    <div class="badge"><span class="badge__dot"></span><span class="badge__name">Velvet Haze</span><span class="badge__flavour">Blueberry</span></div>
  </section>
  <section class="pack pack--bubblegum">
    <div class="smoke" role="img" aria-label="Soft smoke swirl decoration in pink"></div>
    <div class="badge"><span class="badge__dot"></span><span class="badge__name">Velvet Haze</span><span class="badge__flavour">Bubblegum</span></div>
  </section>
  <section class="pack pack--cherry">
    <div class="smoke" role="img" aria-label="Soft smoke swirl decoration in plum"></div>
    <div class="badge"><span class="badge__dot"></span><span class="badge__name">Velvet Haze</span><span class="badge__flavour">Cherry</span></div>
  </section>
  <section class="pack pack--mango">
    <div class="smoke" role="img" aria-label="Soft smoke swirl decoration in orange"></div>
    <div class="badge"><span class="badge__dot"></span><span class="badge__name">Velvet Haze</span><span class="badge__flavour">Mango</span></div>
  </section>
  <section class="pack pack--menthol">
    <div class="smoke" role="img" aria-label="Soft smoke swirl decoration in green"></div>
    <div class="badge"><span class="badge__dot"></span><span class="badge__name">Velvet Haze</span><span class="badge__flavour">Menthol</span></div>
  </section>
  <section class="pack pack--pineapple">
    <div class="smoke" role="img" aria-label="Soft smoke swirl decoration in yellow"></div>
    <div class="badge"><span class="badge__dot"></span><span class="badge__name">Velvet Haze</span><span class="badge__flavour">Pineapple</span></div>
  </section>
  <section class="pack pack--strawberry">
    <div class="smoke" role="img" aria-label="Soft smoke swirl decoration in red"></div>
    <div class="badge"><span class="badge__dot"></span><span class="badge__name">Velvet Haze</span><span class="badge__flavour">Strawberry</span></div>
  </section>
  <span class="dimension dimension--width">9 cm</span>
  <span class="dimension dimension--height">8.5 cm</span>
</main>
</body>
</html>
```